Create a flyer for credit repair

I need a flyer created for credit repair, something that's creative and gets the job done. please include the company logo which is attached and the title of the flyer should be "WHEN YOU CONTROL YOUR CREDIT, YOU CONTROL THE BANKS"
List of removals: collections, charge offs, inquiries, bankruptcy, late payments
The price of the credit repair is $300.
The consumer can receive a $25 rebate if they refer a friend or family member that signs up.
I encourage you to be creative.

Also please add my Instagram name: @Brovenluxo (if possible use Instagram thumbnail)

AT THE VERY BOTTOM OF THE FLYER PLEASE OUT “BOOK YOUR FREE CONSULTATION TODAY!”

```html
<!DOCTYPE html>
<html lang="en">
<head>
<meta charset="utf-8">
<title>Credit Repair Flyer</title>
<link href="https://fonts.googleapis.com/css2?family=Montserrat:wght@500;600;700;800;900&display=swap" rel="stylesheet">
<style>
  :root {
    --page-bg: #e6e7e9;
    --navy: #1c3f8f;
    --navy-deep: #16347a;
    --teal: #1a9d8c;
    --lime: #c6e03a;
    --white: #ffffff;
    --ink: #111111;
    --gold: #b9975b;
  }
  * { margin: 0; padding: 0; box-sizing: border-box; }
  html, body {
    width: 1200px; height: 795px; overflow: hidden;
    background: var(--page-bg);
    font-family: "Montserrat", Arial, sans-serif;
  }
  .flyer {
    position: absolute; left: 340px; top: 30px;
    width: 520px; height: 735px;
    background: var(--white);
    overflow: hidden;
    box-shadow: 0 6px 20px rgba(0,0,0,0.18);
  }
  .flyer-shapes { position: absolute; inset: 0; }
  .headline {
    position: absolute; left: 34px; top: 36px;
    color: var(--white); font-weight: 800; text-transform: uppercase;
    line-height: 1.15;
  }
  .headline .line-small { font-size: 19px; letter-spacing: 0.3px; }
  .headline .line-large { font-size: 27px; }
  .headline .accent { color: var(--lime); }
  .headline-rule {
    position: absolute; left: 34px; top: 108px;
    width: 330px; height: 3px; background: var(--lime);
  }
  .removals {
    position: absolute; left: 34px; top: 126px; color: var(--white);
  }
  .removals h2 { font-size: 21px; font-weight: 800; margin-bottom: 6px; }
  .removals ul { list-style: none; }
  .removals li {
    font-size: 14px; font-weight: 600; line-height: 1.5;
    display: flex; align-items: center; gap: 9px; text-transform: uppercase;
  }
  .removals li::before {
    content: ""; width: 9px; height: 9px; border-radius: 50%;
    background: var(--white);
  }
  .illustration {
    position: absolute; left: 330px; top: 120px;
    width: 120px; height: 110px; border-radius: 8px;
    background: linear-gradient(135deg, #2b2f3a, #6d7482 60%, #d8dbe0);
  }
  .brand-seal {
    position: absolute; left: 380px; top: 205px;
    width: 118px; height: 118px; border-radius: 50%;
    background: var(--white); border: 3px solid var(--navy);
    display: flex; align-items: center; justify-content: center;
  }
  .brand-name {
    width: 84px; text-align: center;
    font-size: 13px; font-weight: 800; line-height: 1.15;
    color: var(--gold); text-transform: uppercase;
  }
  .price-tag {
    position: absolute; left: 0; top: 372px;
    padding: 6px 26px 6px 34px;
    background: var(--teal); color: var(--white);
    font-size: 34px; font-weight: 900; letter-spacing: 1px;
  }
  .price-amount {
    position: absolute; left: 34px; top: 424px;
    color: var(--teal); font-size: 62px; font-weight: 900; line-height: 1;
  }
  .rebate {
    position: absolute; left: 34px; top: 508px; width: 460px;
    text-align: center; color: var(--ink);
  }
  .rebate .lead { font-size: 25px; font-weight: 800; }
  .rebate .badge {
    display: inline-block; margin: 6px 0;
    padding: 4px 22px; background: var(--teal); color: var(--white);
    font-size: 25px; font-weight: 800;
  }
  .rebate .terms { font-size: 14px; font-weight: 600; }
  .cta {
    position: absolute; left: 34px; top: 604px; width: 460px;
    text-align: center;
  }
  .cta .cta-top { color: var(--teal); font-size: 34px; font-weight: 900; line-height: 1.05; }
  .cta .cta-bottom { color: var(--ink); font-size: 22px; font-weight: 800; }
  .social {
    position: absolute; left: 34px; top: 686px; width: 330px;
    display: flex; align-items: center; gap: 10px;
    color: var(--white); font-size: 22px; font-weight: 700;
  }
  .social .dot {
    width: 26px; height: 26px; border-radius: 50%;
    border: 3px solid var(--white);
  }
</style>
</head>
<body>
  <main class="flyer">
    <svg class="flyer-shapes" width="520" height="735" viewBox="0 0 520 735">
      <polygon points="0,0 520,0 520,110 250,340 0,355" fill="var(--navy)"/>
      <polygon points="0,0 180,0 0,120" fill="var(--navy-deep)" opacity="0.5"/>
      <polygon points="0,355 250,340 520,110 520,140 262,362 0,376" fill="var(--teal)"/>
      <polygon points="0,735 0,690 520,650 520,735" fill="var(--teal)"/>
      <polygon points="360,735 520,640 520,735" fill="var(--navy)" opacity="0.25"/>
    </svg>

    <header class="headline">
      <div class="line-small">When you control <span class="accent">your credit,</span></div>
      <div class="line-large">You control <span class="accent">the banks</span></div>
    </header>
    <div class="headline-rule"></div>

    <section class="removals">
      <h2>LIST OF REMOVALS:</h2>
      <ul>
        <li>Collections</li>
        <li>Charge offs</li>
        <li>Inquiries</li>
        <li>Bankruptcy</li>
        <li>Late payments</li>
      </ul>
    </section>

    <div class="illustration" role="img" aria-label="Illustration of a credit card being repaired with a wrench"></div>

    <div class="brand-seal">
      <span class="brand-name">Crestline Credit</span>
    </div>

    <div class="price-tag">PRICE</div>
    <div class="price-amount">$300</div>

    <section class="rebate">
      <div class="lead">The consumer can receive a</div>
      <div class="badge">$25 rebate</div>
      <div class="terms">if they refer a friend or family member that signs up.</div>
    </section>

    <section class="cta">
      <div class="cta-top">BOOK YOUR FREE</div>
      <div class="cta-bottom">CONSULTATION TODAY!</div>
    </section>

    <div class="social">
      <span class="dot"></span>
      <span class="handle">@Brovenluxo</span>
    </div>
  </main>
</body>
</html>
```